ORVILMA card Technical Architecture

Hello everyone ORVILMA: It is a consulting firm in Architecture and Construction. I require a card duplexing, sober, elegant, classic but not boring. Update 1: Use the following data for the card. Name: Rodrigo Salinas Tomás Quevedo Position: COO Twitter: @orvilmaAT Homepage: orvilma.com home address not include the participation of all thank you.

Target Market(s)

Construction companies, Architects and Consulting Engineers

Industry/Entity Type

Consulting

Contact Information for Business Card

Los campos que debe tener:
Nombre, Cargo, email, homepage y twitter

Font styles to use
Serif
Sans Serif
Other font styles liked:
• Me gustan playfair display, open sans y roboto, pero estoy sujeto a sus propuestas

Requirements
Must have
• Colors: Present combined proposals in white, red, gray and black Update 1: The two names must be clearly differentiated from the two surnames
Nice to have
• They are free to present their best proposals. I will bring them immediate feedback to the extent you can go see their designs. Complete data for card and logo files will give the winner the

```html
<!DOCTYPE html>
<html lang="en">
<head>
<meta charset="utf-8">
<title>ORVILMA business card</title>
<link rel="stylesheet" href="https://fonts.googleapis.com/css2?family=Josefin+Sans:wght@300&family=Playfair+Display:wght@400&family=Open+Sans:wght@400;600&display=swap">
<style>
  :root {
    --page: #e6e3df;
    --card: #fbfbfa;
    --ink: #1d1d1d;
    --red: #c8202c;
    --rose: #c99a8c;
    --gray: #555;
  }
  * { margin: 0; padding: 0; box-sizing: border-box; }
  html, body { width: 1200px; height: 902px; overflow: hidden; background: var(--page); }
  .canvas { position: relative; width: 1200px; height: 902px; }
  .card {
    position: absolute;
    width: 580px; height: 332px;
    background: var(--card);
    box-shadow: 0 6px 18px rgba(0,0,0,.18);
  }
  .card--front { left: 90px; top: 80px; }
  .card--back { left: 530px; top: 490px; }

  .lockup { position: absolute; text-align: center; }
  .lockup__name {
    display: flex; align-items: center; justify-content: center; gap: 14px;
    font-family: "Josefin Sans", sans-serif; font-weight: 300;
    color: var(--ink); letter-spacing: .28em;
  }
  .lockup__mark { width: 14px; height: 14px; background: var(--red); flex: none; }
  .lockup__rule { height: 1px; background: var(--rose); margin-top: 8px; }

  .card--front .lockup { left: 0; right: 0; top: 140px; }
  .card--front .lockup__name { font-size: 46px; }
  .card--front .lockup__rule { width: 330px; margin-left: auto; margin-right: auto; }

  .card--back .lockup { left: 20px; width: 250px; top: 150px; }
  .card--back .lockup__name { font-size: 30px; gap: 10px; }
  .card--back .lockup__mark { width: 10px; height: 10px; }

  .divider {
    position: absolute; left: 282px; top: 28px; width: 1.5px; height: 276px;
    background: linear-gradient(to bottom, rgba(200,32,44,0), var(--red) 55%, rgba(200,32,44,0));
  }
  .contact { position: absolute; left: 300px; right: 14px; top: 44px; text-align: center; }
  .contact__name {
    font-family: "Playfair Display", serif; font-weight: 400; font-size: 24px; line-height: 29px;
  }
  .contact__given { display: block; color: var(--red); }
  .contact__surname { display: block; color: var(--ink); }
  .contact__role {
    font-family: "Open Sans", sans-serif; font-weight: 600; font-size: 12px;
    letter-spacing: .2em; color: var(--gray); margin: 8px 0 30px;
  }
  .contact__lines {
    list-style: none;
    font-family: "Open Sans", sans-serif; font-size: 13px; line-height: 20px; color: var(--ink);
  }
</style>
</head>
<body>
<main class="canvas">
  <section class="card card--front" aria-label="Card front">
    <div class="lockup">
      <div class="lockup__name"><span class="lockup__mark"></span>ORVILMA</div>
      <div class="lockup__rule"></div>
    </div>
  </section>

  <section class="card card--back" aria-label="Card back">
    <div class="lockup">
      <div class="lockup__name"><span class="lockup__mark"></span>ORVILMA</div>
      <div class="lockup__rule"></div>
    </div>
    <div class="divider"></div>
    <div class="contact">
      <h1 class="contact__name">
        <span class="contact__given">Rodrigo Salinas</span>
        <span class="contact__surname">Tomás Quevedo</span>
      </h1>
      <p class="contact__role">COO</p>
      <ul class="contact__lines">
        <li>555.204.1187</li>
        <li>rodrigo@orvilma.com</li>
        <li>orvilma.com</li>
        <li>@orvilmaAT</li>
      </ul>
    </div>
  </section>
</main>
</body>
</html>
```